What makes us Different Managed Communications Services Provider Flyer

We need a flyer to explain why we are different than other "managed IT services" company. Gives a brief description of our company and services that can entice clients and potential clients to setup a FREE consultation with us. This will become part of an ongoing marketing campaign that includes emails, leave behinds, brochures, and more

```html
<!DOCTYPE html>
<html lang="en">
<head>
<meta charset="utf-8">
<title>Managed IT Services Flyer</title>
<link href="https://fonts.googleapis.com/css2?family=Jost:wght@400;500;600;700&display=swap" rel="stylesheet">
<style>
  :root{
    --bg:#a9a9a9;
    --paper:#ffffff;
    --ink:#1b1b1b;
    --blue-deep:#1c5fae;
    --blue-mid:#1f86d6;
    --blue-light:#35c3ee;
    --illus-a:#dcecf8;
    --illus-b:#b9d8f1;
  }
  *{box-sizing:border-box;margin:0;padding:0}
  html,body{width:1200px;height:1200px;overflow:hidden}
  body{background:var(--bg);font-family:"Jost",sans-serif;color:var(--ink);position:relative}
  .flyer{position:absolute;left:208px;top:38px;width:783px;height:1104px;background:var(--paper);overflow:hidden}
  .title-band{position:absolute;left:0;top:28px;width:472px;height:156px}
  .title-band svg{position:absolute;inset:0}
  .title{position:absolute;left:40px;top:10px;color:#fff;font-weight:700;font-size:54px;line-height:60px;letter-spacing:.3px}
  .brand{position:absolute;left:540px;top:130px;display:flex;align-items:center;gap:9px}
  .brand-dot{width:22px;height:22px;border-radius:50%;background:var(--blue-mid)}
  .brand-name{font-weight:600;font-size:17px;color:var(--ink);line-height:1}
  .brand-since{position:absolute;left:572px;top:154px;font-size:10px;letter-spacing:2px;font-weight:600;color:var(--ink)}
  h2{font-weight:700;font-size:19px;line-height:24px;margin-bottom:1px}
  p,li{font-size:12.6px;line-height:19.4px;text-align:justify;letter-spacing:-.1px}
  .block{position:absolute}
  .intro{left:40px;top:206px;width:703px}
  .contracts{left:40px;top:366px;width:703px}
  .col-left{left:40px;top:510px;width:322px}
  .col-right{left:406px;top:510px;width:337px}
  .col-right p+p{margin-top:16px}
  .col-right h2.spaced{margin-top:18px}
  ul{list-style:none}
  li{position:relative;padding-left:26px;text-align:left}
  li::before{content:"";position:absolute;left:11px;top:8px;width:4px;height:4px;border-radius:50%;background:var(--ink)}
  .illustration{position:absolute;left:57px;top:842px;width:254px;height:150px;border-radius:8px;background:linear-gradient(135deg,var(--illus-a),var(--illus-b))}
  .cta-band{position:absolute;left:0;top:1006px;width:375px;height:60px}
  .cta-band svg{position:absolute;inset:0}
  .cta-text{position:absolute;left:40px;top:9px;color:#fff;font-weight:600;font-size:30px;line-height:40px}
</style>
</head>
<body>
<main class="flyer">
  <div class="title-band">
    <svg width="472" height="156" viewBox="0 0 472 156" aria-hidden="true">
      <defs>
        <linearGradient id="bandGrad" x1="0" y1="0" x2="1" y2="0">
          <stop offset="0" stop-color="#35c3ee"/>
          <stop offset="1" stop-color="#1c5fae"/>
        </linearGradient>
      </defs>
      <path d="M0 0 H412 Q432 0 440 18 L468 126 Q474 156 442 156 H0 Z" fill="url(#bandGrad)"/>
    </svg>
    <h1 class="title">MANAGED<br>IT SERVICES</h1>
  </div>

  <div class="brand">
    <span class="brand-dot"></span>
    <span class="brand-name">Northline Voice &amp; Data</span>
  </div>
  <div class="brand-since">SINCE 1983</div>

  <section class="block intro">
    <h2>More Than Just a Managed IT Provider – Our Legacy of Excellence</h2>
    <p>At our company, we are far more than your typical managed IT provider. Since our founding in 1983, we have built a reputation based on trust, reliability, and unparalleled service. With client relationships spanning 20 to 30 years, we have demonstrated a level of commitment that few IT firms can match. What sets us apart is not just our technical expertise but the deep, long-term partnerships we cultivate with our clients—many of whom have stayed with us without ever being locked into a contract. That is a testament to the exceptional quality of our service and the trust we have earned over decades.</p>
  </section>

  <section class="block contracts">
    <h2>A Commitment Beyond Contracts</h2>
    <p>Unlike many managed IT providers who rely on rigid contracts to retain clients, we believe that service excellence speaks for itself. The longevity of our client relationships is rooted in our ability to anticipate needs, resolve challenges before they escalate, and proactively enhance network &amp; communication infrastructures. Our comprehensive checklists, questionnaires, policies, and procedures, attention to details ensure that every client receives a tailored, best-in-class experience from day one.</p>
  </section>

  <section class="block col-left">
    <h2>A Holistic Approach to<br>IT Management</h2>
    <p>We don't just manage IT—we integrate ourselves into your business, ensuring that technology aligns with your strategic goals. Our services go beyond traditional break-fix support; we offer:</p>
    <ul>
      <li>Strategic IT Roadmaps customized to drive business growth.</li>
      <li>Proactive cybersecurity assessments that help keep businesses secure.</li>
      <li>Comprehensive backup and disaster recovery solutions that provide peace of mind.</li>
      <li>Industry-leading response times and dedicated support teams focused on delivering an exceptional client experience.</li>
    </ul>
  </section>

  <section class="block col-right">
    <h2>Our Clients Stay Because<br>We Deliver</h2>
    <p>For over 40 years, we have maintained a standard of excellence that other companies simply cannot compare with. Our team of experts consistently goes above and beyond, ensuring that clients not only get the support they need but also receive the strategic guidance necessary to stay ahead in an ever-evolving digital landscape.</p>
    <p>Our 90-day performance review process ensures that we continuously improve our service based on client feedback. This process allows us to adapt, refine, and enhance our approach, providing a truly personalized IT experience that aligns with business objectives.</p>
    <h2 class="spaced">A Legacy of Trust &amp; Reliability</h2>
    <p>The fact that many of our clients have remained with us for decades without a formal contract speaks volumes about the trust we have built. We don't lock in clients with paperwork—we keep them with results. That's the difference between a standard managed IT provider and an IT partner who genuinely cares.</p>
    <p>If you're looking for an IT provider that will treat your business as if it were their own, look no further. Our legacy of service, innovation, and commitment to our clients is what sets us apart from the rest.</p>
  </section>

  <div class="illustration" role="img" aria-label="Illustration of a team working around a large laptop screen with code, surrounded by tech icons and a plant"></div>

  <div class="cta-band">
    <svg width="375" height="60" viewBox="0 0 375 60" aria-hidden="true">
      <defs>
        <linearGradient id="ctaGrad" x1="0" y1="0" x2="1" y2="0">
          <stop offset="0" stop-color="#1c5fae"/>
          <stop offset="1" stop-color="#35c3ee"/>
        </linearGradient>
      </defs>
      <path d="M0 0 H347 Q363 0 367 14 L373 46 Q375 60 359 60 H0 Z" fill="url(#ctaGrad)"/>
    </svg>
    <div class="cta-text">FREE consultation</div>
  </div>
</main>
</body>
</html>
```